Bluewater Motor Finance Home Page

We need a desktop version mock up (we will base our mobile version off of this) of a website homepage for our auto loan business, Bluewater Motor Finance. This does not need to be a functioning site, just a home page mock up. We are based in the metro St. Louis, MO area. We offer "guaranteed" auto loans for all credit types. We specialize in financing for bad/no credit customers. We are able to help rebuild these type of customers' credit, all while putting them in a great late model vehicle they'll love. Our online credit app takes less than 60 seconds, doesn't require a SS# and gives a free credit score if they fill it out within 3 minutes. We are looking for an outside perspective to help us in this design process. We are not completely sure what we want, but we do want it to be professional and secure looking, all while being unique and aesthetically pleasing. We want the customer to be able to put in their zip code to be directed to the right location that can get them pre approved. I attached a wireframe with some stuff we'd like to include, but in no way does it have to be in the same layout or the same ideas. We want everyone to "go crazy" with their creative side on this. Our current site is awful, here is a link to get a better idea: www.bluewatermotorfinance-example.com. Attached is our logo too, base colors off of it. Watch our video that is also attached for a better idea.

Target Market(s)

Residents of the St. Louis Missouri Metro Area that need an auto loan. 24-55 Male and Female - Lots of "urban market" customers.

Industry/Entity Type

Loan

Number of Pages Required

1 page

Colors
9bcb3b

Requirements
Must have
• An area where the customer can enter their zip code - Be creative!
Nice to have
• See wireframe attachment for ideas - Be creative!

```html
<!DOCTYPE html>
<html lang="en">
<head>
<meta charset="utf-8">
<title>Bluewater Motor Finance — Home</title>
<link href="https://fonts.googleapis.com/css2?family=Open+Sans:ital,wght@0,400;0,600;0,700;1,400&family=Oswald:wght@400;700&display=swap" rel="stylesheet">
<style>
:root{
  --green:#37a865;
  --green-dark:#235c3c;
  --navy:#1c1c2c;
  --red:#e9585a;
  --gray:#a9a9a9;
  --ink:#222;
  --white:#fff;
  --field:#ececec;
  --phone:#f2e600;
}
*{box-sizing:border-box;margin:0;padding:0}
html,body{width:1200px;height:2691px;overflow:hidden}
body{font-family:"Open Sans",Arial,sans-serif;color:var(--white);position:relative;background:var(--white)}
section,header,footer{position:absolute;left:0;width:1200px}
.abs{position:absolute}
.center{left:0;width:1200px;text-align:center}

/* header */
.site-header{top:0;height:112px;background:var(--green)}
.brand{left:99px;top:34px;display:flex;align-items:center;gap:12px;font-weight:700;font-size:24px;color:var(--white)}
.brand-dot{width:34px;height:34px;border-radius:50%;background:var(--white)}
.header-phone{right:100px;top:20px;font-size:24px;color:var(--phone);display:flex;align-items:center;gap:10px}
.main-nav{right:98px;top:64px;display:flex;gap:53px;font-size:17px}

/* hero */
.hero{top:112px;height:403px;background:var(--navy)}
.hero-title{left:97px;top:92px;font-size:30px;font-weight:700}
.hero-sub{left:99px;top:155px;font-size:19px}
.zip-form{left:102px;top:240px;display:flex}
.zip-input{width:271px;height:44px;background:var(--white);border:1px solid #ddd;border-radius:3px 0 0 3px}
.zip-btn{width:172px;height:44px;background:var(--red);font-size:15px;display:flex;align-items:center;justify-content:center;border-radius:0 3px 3px 0}
.video-slab{left:622px;top:72px;width:478px;height:273px;background:#444;transform:skewY(1deg)}
.video{left:630px;top:62px;width:470px;height:272px;background:var(--white);border-radius:6px;color:#111;text-align:center;box-shadow:-6px 8px 0 #555}
.video-brand{margin-top:22px;font-family:"Oswald",sans-serif;font-size:26px;font-weight:700;color:#1f8a3a}
.video-rule{margin:10px auto 0;width:386px;height:3px;background:#111}
.video-line1{font-family:"Oswald",sans-serif;font-size:40px;line-height:44px;margin-top:6px}
.video-line2{font-family:"Oswald",sans-serif;font-size:56px;font-weight:700;line-height:54px;color:#1f9a2c}
.video-line3{font-family:"Oswald",sans-serif;font-size:40px;line-height:40px}
.video-bar{left:14px;bottom:10px;width:442px;height:14px;background:#222;border-radius:2px}

/* section headings */
.sec-title{font-size:23px}
.sec-sub{font-size:14px}
.divider{left:484px;width:232px;height:12px}

/* steps */
.steps{top:515px;height:473px;background:var(--green)}
.step{top:190px;width:190px;text-align:center}
.step-num{font-size:44px;font-weight:700;line-height:52px}
.step-text{margin-top:14px;font-size:10.5px;line-height:15.5px}

/* credit score band */
.score-band{top:988px;height:354px;background:var(--gray);color:#111}
.score-title{top:100px;font-size:39px}
.score-sub{top:150px;font-size:18px;line-height:18px}
.calc-btn{left:513px;top:221px;width:172px;height:45px;background:var(--red);color:var(--white);font-size:14px;display:flex;align-items:center;justify-content:center;border-radius:2px}

/* testimonials */
.testimonials{top:1345px;height:619px;background:var(--white);color:var(--ink)}
.avatar{left:140px;top:230px;width:226px;height:226px;border-radius:50%;background:#7a7a7a;border:4px solid #e6e6e6}
.quote{left:449px;top:280px;width:654px;font-size:16px;font-style:italic;line-height:27px;color:#333}
.quote-mark{left:443px;top:268px;font-size:30px;color:#333;font-family:Georgia,serif}
.quote-name{left:474px;top:371px;font-size:20px;font-weight:700}
.dots{left:546px;top:515px;display:flex;gap:12px}
.dot{width:20px;height:20px;border-radius:50%;background:#777}
.dot.is-active{background:#333}

/* contact */
.contact{top:1964px;height:575px;background:var(--green)}
.office{left:98px;top:248px;font-size:16px;line-height:20px}
.office h3{font-size:16px;font-weight:700;margin-bottom:14px}
.office-row{display:flex;align-items:center;gap:8px;margin-top:16px}
.socials{left:102px;top:420px;display:flex;gap:16px}
.social{width:30px;height:30px;border-radius:50%;background:var(--white)}
.social.muted{opacity:.45}
.field{background:var(--field);color:#888;font-size:15px;padding:14px 18px;border-radius:2px}
.send-btn{left:613px;top:447px;width:132px;height:47px;background:var(--red);font-size:16px;display:flex;align-items:center;justify-content:center;border-radius:2px}
.to-top{left:1123px;top:494px;width:49px;height:48px;background:#bfbfbf}

/* footer */
.site-footer{top:2539px;height:152px;background:var(--green-dark)}
.footer-nav{top:32px;display:flex;justify-content:center;gap:53px;font-size:17px}
.footer-brand{top:72px;font-size:17px;font-weight:700}
.copyright{top:114px;font-size:11px}
</style>
</head>
<body>

<header class="site-header">
  <div class="abs brand"><span class="brand-dot"></span>Bluewater Motor Finance</div>
  <div class="abs header-phone">(800) 555-0142
    <svg width="26" height="26" viewBox="0 0 24 24"><path fill="#f2e600" d="M6.6 10.8a15 15 0 0 0 6.6 6.6l2.2-2.2a1 1 0 0 1 1-.25 11.4 11.4 0 0 0 3.6.57 1 1 0 0 1 1 1V20a1 1 0 0 1-1 1A17 17 0 0 1 3 4a1 1 0 0 1 1-1h3.5a1 1 0 0 1 1 1c0 1.25.2 2.45.57 3.57a1 1 0 0 1-.25 1z"/></svg>
  </div>
  <nav class="abs main-nav"><span>Home</span><span>Locations</span><span>Finance Center</span><span>FAQ</span><span>Contact</span></nav>
</header>

<section class="hero">
  <h1 class="abs hero-title">Over 30,000 Auto Loans Since 2000</h1>
  <p class="abs hero-sub">Pre-Approval in Under 60 Seconds!</p>
  <div class="abs zip-form"><div class="zip-input"></div><div class="zip-btn">Get approved!</div></div>
  <div class="abs video">
    <div class="video-brand">BLUEWATER MOTOR FINANCE</div>
    <div class="video-rule"></div>
    <div class="video-line1">10 Minute</div>
    <div class="video-line2">GUARANTEED</div>
    <div class="video-line3">Approval</div>
    <svg class="abs video-bar" viewBox="0 0 442 14">
      <rect width="442" height="14" fill="#222"/>
      <rect x="8" y="4" width="3" height="7" fill="#ddd"/><rect x="13" y="4" width="3" height="7" fill="#ddd"/>
      <rect x="26" y="6" width="300" height="2" fill="#888"/><rect x="26" y="6" width="160" height="2" fill="#eee"/>
      <circle cx="186" cy="7" r="3" fill="#fff"/>
      <rect x="360" y="6" width="40" height="2" fill="#eee"/>
      <rect x="420" y="4" width="10" height="7" fill="none" stroke="#ddd"/>
    </svg>
  </div>
</section>

<section class="steps">
  <h2 class="abs center sec-title" style="top:57px">Steps to SUCESS</h2>
  <p class="abs center sec-sub" style="top:92px">Lorem ipsum dolor sit amet, consectetur adipiscing e</p>
  <svg class="abs divider" style="top:121px" viewBox="0 0 232 12"><line x1="6" y1="6" x2="226" y2="6" stroke="#fff" stroke-width="2"/><circle cx="6" cy="6" r="5" fill="#fff"/><circle cx="226" cy="6" r="5" fill="#fff"/></svg>
  <div class="abs step" style="left:124px"><div class="step-num">1</div><p class="step-text">Enter your zip code in the secure form above. We match you with the nearest branch ready to review your application and help you get started today.</p></div>
  <div class="abs step" style="left:375px"><div class="step-num">2</div><p class="step-text">Fill out our short credit application in under sixty seconds. No Social Security number is required, and every credit type is welcome, including bad or no credit.</p></div>
  <div class="abs step" style="left:637px"><div class="step-num">3</div><p class="step-text">Receive your guaranteed approval and a free credit score. Our finance team walks you through terms, payments and options that fit your monthly budget with no surprises.</p></div>
  <div class="abs step" style="left:890px"><div class="step-num">4</div><p class="step-text">Drive home in a great late model vehicle you will love. Make payments on time and rebuild your credit with every month behind the wheel of your car.</p></div>
</section>

<section class="score-band">
  <h2 class="abs center score-title">Apply within <strong>3:00</strong> and see your credit score for free!</h2>
  <p class="abs center score-sub">Lorem ipsum dolor sit amet, consectetur adipiscing elit.<br>Proin a elit vitae erat accumsan.</p>
  <div class="abs calc-btn">Calculate Pament</div>
</section>

<section class="testimonials">
  <h2 class="abs center sec-title" style="top:94px;font-weight:600;font-size:26px">What Our Happy Customer Say</h2>
  <p class="abs center sec-sub" style="top:138px;font-size:15px">lorem ipsum dolor sit amet</p>
  <svg class="abs divider" style="top:174px" viewBox="0 0 232 12"><line x1="6" y1="6" x2="226" y2="6" stroke="#333" stroke-width="2"/><circle cx="6" cy="6" r="5" fill="#333"/><circle cx="226" cy="6" r="5" fill="#333"/></svg>
  <div class="abs avatar" role="img" aria-label="Customer portrait"></div>
  <span class="abs quote-mark">“</span>
  <p class="abs quote">&nbsp;&nbsp;&nbsp;Lorem ipsum dolor sit amet, consectetur adipiscing elit. Proin a elit vitae erat accumsan venenatis in itur velit. dapibus fringilla! Lorem ipsum dolor sit amet, consectetur adipiscing elit. Proin a elit vitae erat accumsan venenatis in ecitur velit. dapibus fringilla!</p>
  <p class="abs quote-name">John Doe</p>
  <div class="abs dots"><span class="dot"></span><span class="dot"></span><span class="dot"></span><span class="dot is-active"></span></div>
</section>

<section class="contact">
  <h2 class="abs center sec-title" style="top:80px;font-weight:700;font-size:27px">Contact</h2>
  <p class="abs center sec-sub" style="top:118px;font-size:15px">Let's talk business, get in touch!</p>
  <svg class="abs divider" style="top:150px" viewBox="0 0 232 12"><line x1="6" y1="6" x2="226" y2="6" stroke="#fff" stroke-width="2"/><circle cx="6" cy="6" r="5" fill="#fff"/><circle cx="226" cy="6" r="5" fill="#fff"/></svg>
  <div class="abs office">
    <h3>Office Hours</h3>
    <div>Monday to Friday / 7:00 - 18:00 Saturday / 9:00 - 15:00</div>
    <div class="office-row"><svg width="14" height="14" viewBox="0 0 24 24"><path fill="#fff" d="M6.6 10.8a15 15 0 0 0 6.6 6.6l2.2-2.2a1 1 0 0 1 1-.25 11.4 11.4 0 0 0 3.6.57 1 1 0 0 1 1 1V20a1 1 0 0 1-1 1A17 17 0 0 1 3 4a1 1 0 0 1 1-1h3.5a1 1 0 0 1 1 1c0 1.25.2 2.45.57 3.57a1 1 0 0 1-.25 1z"/></svg>(800) 555-0142</div>
    <div class="office-row"><svg width="16" height="12" viewBox="0 0 16 12"><rect width="16" height="12" fill="#fff"/><path d="M0 0l8 6 8-6" fill="none" stroke="#37a865" stroke-width="1.5"/></svg>XXX@XXXXXX.com</div>
  </div>
  <div class="abs socials"><span class="social"></span><span class="social muted"></span><span class="social muted"></span></div>
  <div class="abs field" style="left:613px;top:221px;width:234px;height:50px">Name</div>
  <div class="abs field" style="left:866px;top:221px;width:234px;height:50px">Email (will not published)</div>
  <div class="abs field" style="left:613px;top:289px;width:487px;height:138px">Message</div>
  <div class="abs send-btn">Send</div>
  <svg class="abs to-top" viewBox="0 0 49 48"><rect width="49" height="48" fill="#bfbfbf"/><path d="M13 30l11.5-11 11.5 11" fill="none" stroke="#777" stroke-width="3"/></svg>
</section>

<footer class="site-footer">
  <nav class="abs footer-nav center"><span>Home</span><span>Locations</span><span>Finance Center</span><span>FAQ</span><span>Contact</span></nav>
  <div class="abs center footer-brand">Bluewater Motor Finance</div>
  <p class="abs center copyright">(c) copyright 2016 Bluewater Motor Finance</p>
</footer>

</body>
</html>
```